ALL TEXT GRAPHICS TM May 2025 for Instagram

We are looking for a series of social media graphics for Instagram (new size: 4:5 (1080 x 1350 pixels) ratio that are ALL TEXT. We want the following quotes below on each graphic; one quote per graphic. AND, In very small letters at the bottom of each graphic, add @TovaMarshOnline
The look and feel of these graphics should be complimentary to the color palette attached below; but keep them simple. But the design is up to you; at the end of this document, I provided various samples of all text graphics that I like as examples.
Target Market(s)
women looking to lose weight
Look and feel

```html
<!DOCTYPE html>
<html lang="en">
<head>
<meta charset="utf-8">
<title>TM All-Text Instagram Series</title>
<link href="https://fonts.googleapis.com/css2?family=Didact+Gothic&family=Nunito:wght@900&display=swap" rel="stylesheet">
<style>
  :root{
    --board:#dcdcdc;
    --board-edge:#555;
    --pink:#ff0a8c;
    --ink:#1c1c1c;
    --card-center:#ffd6ea;
    --card-edge:#ff9ccb;
  }
  *{margin:0;padding:0;box-sizing:border-box}
  html,body{width:1200px;height:849px;overflow:hidden;background:var(--board)}
  .board{position:relative;width:1200px;height:849px;border:1px solid var(--board-edge);background:var(--board)}
  .post{
    position:absolute;width:217px;height:272px;
    background:radial-gradient(ellipse 70% 60% at 50% 52%,var(--card-center) 20%,var(--card-edge) 100%);
    font-family:"Didact Gothic",sans-serif;color:var(--ink);
  }
  .row-1{top:141px}
  .row-2{top:435px}
  .col-1{left:37px}.col-2{left:264px}.col-3{left:491px}.col-4{left:718px}.col-5{left:946px}
  .block{position:absolute;white-space:nowrap}
  .headline{font-size:28px;line-height:30px;letter-spacing:.2px}
  .accent{font-family:"Nunito",sans-serif;font-weight:900;color:var(--pink)}
  .kicker{font-size:18px;line-height:20px}
  .body{font-size:13.5px;line-height:17.5px}
  .mid{font-size:19px;line-height:24px}
  .footer{position:absolute;bottom:13px;font-size:13.5px;line-height:17.5px}
  .footer .accent{font-size:13.5px}
  .mega{font-size:92px;line-height:72px;letter-spacing:-2px}
  .large{font-size:52px;line-height:48px}
</style>
</head>
<body>
<main class="board">

  <!-- Row 1 -->
  <article class="post row-1 col-1">
    <div class="block headline" style="left:44px;top:17px">Tired.<br>Moody.</div>
    <div class="block kicker accent" style="left:44px;top:83px">Stubborn<br>Belly Fat.</div>
    <div class="block body" style="left:44px;top:142px">Your hormones are<br>screaming for help!</div>
    <div class="footer" style="left:44px"><span class="accent">Let's fix that.</span><br>@TovaMarshOnline</div>
  </article>

  <article class="post row-1 col-2">
    <div class="block headline" style="left:27px;top:17px">That<br>stubborn<br>weight?</div>
    <div class="block kicker accent" style="left:27px;top:113px">It's not<br>your fault.</div>
    <div class="block body" style="left:27px;top:172px">Your hormones are to<br>blame and you're not<br>alone; <span class="accent">But there is a fix.</span></div>
    <div class="footer" style="left:27px">@TovaMarshOnline</div>
  </article>

  <article class="post row-1 col-3">
    <div class="block headline" style="left:29px;top:17px">Your belly<br>isn't fat...</div>
    <div class="block kicker accent" style="left:29px;top:83px">it's hormonal.</div>
    <div class="block body" style="left:29px;top:120px">And here's how to fix it.<br>Comment <span class="accent">HORMONES</span><br>if nothing is working.</div>
    <div class="footer" style="left:29px">@TovaMarshOnline</div>
  </article>

  <article class="post row-1 col-4">
    <div class="block headline" style="left:20px;top:17px">The stubborn<br>belly fat after</div>
    <div class="block mega accent" style="left:18px;top:86px">40?</div>
    <div class="block body" style="left:20px;top:158px">It's not about calories;<br>it's about your hormones.</div>
    <div class="footer" style="left:20px"><span class="accent">Here is the fix!</span><br>@TovaMarshOnline</div>
  </article>

  <article class="post row-1 col-5">
    <div class="block headline" style="left:14px;top:17px">Flat tummy<br>in <span class="accent">your 40s?</span></div>
    <div class="block kicker accent" style="left:14px;top:83px">It's still possible!</div>
    <div class="block body" style="left:14px;top:120px">Comment <span class="accent">BYE BELLY</span> to get<br>the <span class="accent">10 secrets</span> to a flatter<br>tummy.</div>
    <div class="footer" style="left:14px">@TovaMarshOnline</div>
  </article>

  <!-- Row 2 -->
  <article class="post row-2 col-1">
    <div class="block headline" style="left:21px;top:17px">Bloating.<br>Muffin top.</div>
    <div class="block kicker accent" style="left:21px;top:83px">It's still possible!</div>
    <div class="block kicker accent" style="left:21px;top:120px;font-size:19px">Puffy waistline.</div>
    <div class="block body" style="left:21px;top:142px">Your body's screaming for<br>a different kind of fix.</div>
    <div class="footer" style="left:21px"><span class="accent">Here it is...</span><br>@TovaMarshOnline</div>
  </article>

  <article class="post row-2 col-2">
    <div class="block headline" style="left:9px;top:17px">You're doing<br>all the <span class="accent">“right”</span><br>things, but</div>
    <div class="block kicker accent" style="left:9px;top:132px;font-size:19px">your belly won't<br>go down?</div>
    <div class="footer" style="left:9px"><span class="accent">Here's what you haven't tried.</span><br>@TovaMarshOnline</div>
  </article>

  <article class="post row-2 col-3">
    <div class="block headline" style="left:17px;top:17px">This <span class="accent">90-day</span><br><span class="accent">plan</span> helped<br>women</div>
    <div class="block mid" style="left:17px;top:130px">over <span class="accent">40 slim down</span>,<br>get <span class="accent">a tiny waist</span><br>and <span class="accent">feel sexy again</span>.</div>
    <div class="footer" style="left:17px"><span class="accent">You're next.</span><br>@TovaMarshOnline</div>
  </article>

  <article class="post row-2 col-4">
    <div class="block headline" style="left:12px;top:17px">This is the<br>secret women</div>
    <div class="block large accent" style="left:11px;top:78px">over 40</div>
    <div class="block body" style="left:12px;top:132px">are using to get snatched;<br>without starving.</div>
    <div class="block body" style="left:12px;top:182px">Comment <span class="accent">SKINNY</span><br>to get the exact plan.</div>
    <div class="footer" style="left:12px">@TovaMarshOnline</div>
  </article>

  <article class="post row-2 col-5">
    <div class="block headline" style="left:12px;top:20px;letter-spacing:-.5px">What worked in</div>
    <div class="block large accent" style="left:11px;top:55px;font-size:48px">your 30s</div>
    <div class="block headline" style="left:12px;top:101px;font-size:26px">won't work now.</div>
    <div class="block body" style="left:12px;top:146px">Here's what actually does.<br><span class="accent">Drop 30 Pounds in 3 Months.</span></div>
    <div class="footer" style="left:12px">@TovaMarshOnline</div>
  </article>

</main>
</body>
</html>
```